Printing company needs website!

A printing company would like a new professional website (made with wix). Now they don't have a website, but they want a unique, beautiful, clear site. Of course they provide the content themselves, we are now looking for the beautiful design with some mockups. You can see several of their projects on their instagram & facebook.
Www.pagenook.com/velmoor and https://www.snapfolio.com/velmoor.be/ logos are attached.

```html
<!DOCTYPE html>
<html lang="nl">
<head>
<meta charset="utf-8">
<title>Velmoor – waar alles velmoor is</title>
<link href="https://fonts.googleapis.com/css2?family=Outfit:wght@400;500;600&family=Montserrat:ital,wght@0,400;1,400&display=swap" rel="stylesheet">
<style>
:root{
  --teal:#4dbaa8;
  --teal-dark:#2f9e8a;
  --yellow:#f5c518;
  --blue:#1e9ad6;
  --ink:#111111;
  --text:#444444;
  --grey-bg:#f0f0f0;
  --footer:#231f20;
  --white:#ffffff;
}
*{margin:0;padding:0;box-sizing:border-box}
html,body{width:1200px;height:2997px;overflow:hidden;background:var(--white)}
body{position:relative;font-family:"Montserrat",sans-serif;color:var(--text)}
.abs{position:absolute}
.heading{font-family:"Outfit",sans-serif;font-weight:500;color:var(--ink)}
.top-stripe{top:0;height:7px}
.brand{display:flex;align-items:center;gap:10px;font-family:"Outfit",sans-serif;font-weight:600;color:var(--ink)}
.brand-dot{width:30px;height:30px;border-radius:50%;background:var(--teal);flex:none}
.brand-tag{font-family:"Outfit",sans-serif;font-size:13px;color:var(--teal)}
.phone-line{font-family:"Outfit",sans-serif;color:var(--yellow);display:flex;align-items:center;gap:8px}
.nav{top:80px;font-family:"Outfit",sans-serif;font-size:17px;font-weight:500;color:#333}
.nav.active{color:var(--teal)}
.btn{display:flex;align-items:center;justify-content:center;background:var(--teal);color:var(--white);font-family:"Outfit",sans-serif;font-weight:500;font-size:19px;border-radius:0 25px 25px 0;text-transform:uppercase}
.hero{top:121px;left:0;width:1200px;height:615px;background:#000;overflow:hidden}
.hero-photo{position:absolute;left:360px;top:0;width:840px;height:615px;background:linear-gradient(110deg,#000 0%,#5a0b3a 18%,#d3186d 32%,#f3731e 48%,#f6d21c 62%,#3fb5d8 76%,#e7d1c1 88%,#f2f2f2 100%);-webkit-mask:linear-gradient(90deg,transparent 0,#000 25%);mask:linear-gradient(90deg,transparent 0,#000 25%)}
.section-intro{font-size:15.5px;line-height:19.5px;text-align:center}
.work-card{top:1108px;width:228px;height:307px;border-radius:12px}
.arrow{width:30px;height:46px}
.about{top:1504px;left:0;width:1200px;height:569px;background:var(--grey-bg);overflow:hidden}
.about p{font-size:15.5px;line-height:19px;color:#555}
.quote{font-style:italic;font-size:20.5px;line-height:27px;color:#555;text-align:center}
.footer{top:2557px;left:0;width:1200px;height:440px;background:var(--footer)}
.field{border:1px solid #8a8a8a;border-radius:0 24px 24px 0;color:#ddd;font-family:"Outfit",sans-serif;font-size:14px;padding:0 12px;display:flex;align-items:center}
.contact-info{font-family:"Outfit",sans-serif;font-size:16px;color:var(--yellow);display:flex;align-items:center;gap:6px;font-weight:500}
.icon-badge{width:24px;height:24px;border-radius:50%;background:var(--yellow);display:flex;align-items:center;justify-content:center;flex:none}
.social{width:48px;height:48px;border:2px solid var(--teal);border-radius:50%}
</style>
</head>
<body>

<div class="abs top-stripe" style="left:0;width:456px;background:var(--teal)"></div>
<div class="abs top-stripe" style="left:456px;width:380px;background:var(--yellow)"></div>
<div class="abs top-stripe" style="left:836px;width:364px;background:var(--blue)"></div>

<header>
  <div class="abs" style="left:131px;top:38px">
    <div class="brand" style="font-size:48px;line-height:48px"><span class="brand-dot"></span>Velmoor</div>
    <div class="brand-tag" style="margin-left:132px;margin-top:-2px">waar alles velmoor is</div>
  </div>
  <div class="abs phone-line" style="left:801px;top:30px;font-size:22px">
    <span class="icon-badge" style="width:26px;height:26px"><svg width="14" height="14" viewBox="0 0 24 24"><path fill="#fff" d="M6.6 10.8a15 15 0 0 0 6.6 6.6l2.2-2.2c.3-.3.7-.4 1-.2 1.1.4 2.3.6 3.6.6.6 0 1 .4 1 1V20c0 .6-.4 1-1 1A17 17 0 0 1 3 4c0-.6.4-1 1-1h3.5c.6 0 1 .4 1 1 0 1.3.2 2.5.6 3.6.1.3 0 .7-.2 1z"/></svg></span>
    Call Us: 0470 12 34 56
  </div>
  <nav>
    <span class="abs nav active" style="left:499px">Home</span>
    <span class="abs nav" style="left:584px">About</span>
    <span class="abs nav" style="left:667px">Services</span>
    <span class="abs nav" style="left:768px">Products</span>
    <span class="abs nav" style="left:871px">Testimonials</span>
    <span class="abs nav" style="left:1001px">Contact</span>
  </nav>
</header>

<section class="abs hero">
  <div class="hero-photo" role="img" aria-label="Photo of a hand holding a pencil over a fanned-out colour swatch book"></div>
  <h1 class="abs heading" style="left:146px;top:200px;font-size:88px;color:var(--white);font-weight:500">Velmoor</h1>
  <p class="abs" style="left:148px;top:306px;font-family:'Outfit',sans-serif;font-size:35px;color:var(--teal)">waar alles velmoor is</p>
  <div class="abs btn" style="left:150px;top:370px;width:160px;height:49px">Read more</div>
</section>
<svg class="abs" style="left:0;top:520px" width="1200" height="245" viewBox="0 0 1200 245">
  <path d="M370 229 H950 C1080 229 1180 150 1200 30" fill="none" stroke="var(--teal)" stroke-width="24" stroke-linecap="round"/>
</svg>

<section>
  <h2 class="abs heading" style="left:0;width:1200px;text-align:center;top:878px;font-size:45px">Latest Velmoor Works</h2>
  <p class="abs section-intro" style="left:200px;width:800px;top:960px">Lorem ipsum dolor sit amet, consectetur adipiscing elit, sed do eiusmod tempor incididunt ut labore et dolore magna aliqua. Quis ipsum suspendisse ultrices gravida. Risus commodo viverra maecenas accumsan lacus Lorem ipsum dolor sit amet, consectetur adipiscing elit, sed do eiusmod tempor incididunt ut labore et dolore magna aliqua. Quis ipsum suspendisse ultrices gravida</p>
  <svg class="abs arrow" style="left:42px;top:1244px" viewBox="0 0 30 46"><path d="M24 4 6 23l18 19" fill="none" stroke="#333" stroke-width="4"/></svg>
  <div class="abs work-card" style="left:122px;background:linear-gradient(160deg,#2a2a2a,#1c1c1c)" role="img" aria-label="Holiday post with festive decoration on a dark background"></div>
  <div class="abs work-card" style="left:365px;background:linear-gradient(180deg,#f1cd2f,#e8c52b)" role="img" aria-label="Sticker promotion post showing printed coffee packaging"></div>
  <div class="abs work-card" style="left:608px;background:linear-gradient(180deg,#4fb8a7,#4bb3a3)" role="img" aria-label="Roll-up banner promotion post"></div>
  <div class="abs work-card" style="left:851px;background:linear-gradient(180deg,#5ba8d2,#8ab0b8)" role="img" aria-label="Cardboard counter display promotion post"></div>
  <svg class="abs arrow" style="left:1110px;top:1244px" viewBox="0 0 30 46"><path d="M6 4l18 19L6 42" fill="none" stroke="#333" stroke-width="4"/></svg>
</section>

<section class="abs about">
  <div class="abs" style="left:-60px;top:300px;width:500px;height:300px;border-radius:50%;background:radial-gradient(ellipse,rgba(160,190,230,.45),rgba(240,200,220,.25) 55%,transparent 72%)" role="img" aria-label="Soft pastel paint swirl decoration"></div>
  <h2 class="abs heading" style="left:119px;top:130px;font-size:45px">About Velmoor</h2>
  <p class="abs" style="left:119px;top:213px;width:495px">Lorem ipsum dolor sit amet, consectetur adipiscing elit, sed do eiusmod tempor incididunt ut labore et dolore magna aliqua. Quis ipsum suspendisse ultrices gravida. Risus comm odo viverra maecenas accumsan lacus vel facilisis.</p>
  <p class="abs" style="left:119px;top:307px;width:495px">Lorem ipsum dolor sit amet, consectetur adipiscing elit, sed do eiusmod tempor incididunt ut labore et dolore magna aliqua. Quis ipsum suspendisse ultrices gravida. Risus comm odo viverra maecenas accumsan lacus vel facilisis.</p>
  <div class="abs btn" style="left:119px;top:413px;width:159px;height:49px">Read more</div>
  <div class="abs" style="left:660px;top:81px;width:434px;height:431px;border-radius:16px;background:linear-gradient(180deg,#5cc2b1 0%,#3fa996 100%)" role="img" aria-label="Photo of a printing press in operation"></div>
</section>

<section>
  <h2 class="abs heading" style="left:0;width:1200px;text-align:center;top:2201px;font-size:45px">Customers are say</h2>
  <svg class="abs arrow" style="left:122px;top:2282px" viewBox="0 0 30 46"><path d="M24 4 6 23l18 19" fill="none" stroke="#333" stroke-width="4"/></svg>
  <p class="abs quote" style="left:225px;width:750px;top:2288px">Lorem ipsum dolor sit amet, consectetur adipiscing elit, sed do eiusmod tempor incididunt ut labore et dolore magna aliqua. Quis ipsum suspendi sse ultrices gravida. Risus comm odo viverra maecenas acc</p>
  <p class="abs" style="left:0;width:1200px;text-align:center;top:2399px;font-family:'Outfit',sans-serif;font-size:17px;font-weight:500;color:var(--teal);text-transform:uppercase">Lena Maris</p>
  <svg class="abs arrow" style="left:1052px;top:2277px" viewBox="0 0 30 46"><path d="M6 4l18 19L6 42" fill="none" stroke="#333" stroke-width="4"/></svg>
</section>

<footer class="abs footer">
  <div class="abs" style="left:157px;top:88px">
    <div class="brand" style="font-size:50px;line-height:50px;color:var(--white)"><span class="brand-dot"></span>Velmoor</div>
    <div class="brand-tag" style="margin-left:142px">waar alles velmoor is</div>
  </div>
  <p class="abs" style="left:180px;width:320px;top:199px;font-size:13px;line-height:19px;color:#aaa;text-align:center">Lorem ipsum dolor sit amet, consectetur adipi scing elit, sed do eiusmod tempor incididunt ut labore et dolore magna aliquauis ipsum</p>
  <a class="abs social" style="left:269px;top:268px" href="https://www.pagenook.com/velmoor" aria-label="Velmoor on Pagenook"></a>
  <a class="abs social" style="left:325px;top:268px" href="https://www.snapfolio.com/velmoor.be/" aria-label="Velmoor on Snapfolio"></a>

  <h3 class="abs" style="left:558px;top:62px;font-family:'Outfit',sans-serif;font-weight:500;font-size:24px;color:var(--white)">Contact Us</h3>
  <div class="abs field" style="left:555px;top:109px;width:223px;height:46px">Name</div>
  <div class="abs field" style="left:555px;top:164px;width:223px;height:46px">Email</div>
  <div class="abs field" style="left:555px;top:220px;width:223px;height:46px">Phone</div>
  <div class="abs field" style="left:788px;top:109px;width:261px;height:101px;align-items:flex-start;padding-top:14px">Message</div>
  <div class="abs btn" style="left:794px;top:221px;width:256px;height:44px;border-radius:22px;font-size:18px">Submit now</div>

  <div class="abs contact-info" style="left:570px;top:319px">
    <span class="icon-badge"><svg width="13" height="10" viewBox="0 0 13 10"><rect x=".5" y=".5" width="12" height="9" rx="1" fill="none" stroke="#231f20"/><path d="M1 1l5.5 4.5L12 1" fill="none" stroke="#231f20"/></svg></span>
    Email:info@velmoor.be
  </div>
  <div class="abs contact-info" style="left:839px;top:319px">
    <span class="icon-badge"><svg width="13" height="13" viewBox="0 0 24 24"><path fill="#231f20" d="M6.6 10.8a15 15 0 0 0 6.6 6.6l2.2-2.2c.3-.3.7-.4 1-.2 1.1.4 2.3.6 3.6.6.6 0 1 .4 1 1V20c0 .6-.4 1-1 1A17 17 0 0 1 3 4c0-.6.4-1 1-1h3.5c.6 0 1 .4 1 1 0 1.3.2 2.5.6 3.6.1.3 0 .7-.2 1z"/></svg></span>
    Call Us: 0470 12 34 56
  </div>
  <p class="abs" style="left:0;width:1200px;text-align:center;top:393px;font-family:'Outfit',sans-serif;font-size:13px;color:#ddd">Copyrights © 2022 All Rights Reversed</p>
</footer>
<svg class="abs" style="left:0;top:2520px" width="860" height="330" viewBox="0 0 860 330">
  <path d="M830 13 H240 C120 13 30 90 0 300" fill="none" stroke="var(--teal)" stroke-width="24" stroke-linecap="round"/>
</svg>

</body>
</html>
```